KVRD Pinecrest Rehabilitation Consultants, INC
Business Card and Stationary for KVRD Pinecrest Rehabilitation
Professional
Dorian K. Lumbard, Ph. D.
Vocational Rehabilitation Consultant
4173b GA Hwy 508 STE 612 Conyers, GA 30081
Dorian.Lumbard@kvrdpinecrestrehab.example
www.kvrdpinecrestrehab.example
I will need whole set of stationary, letterhead, envelopes etc.

```html
<!DOCTYPE html>
<html lang="en">
<head>
<meta charset="utf-8">
<title>KVRD Pinecrest Rehabilitation — Business Card</title>
<link rel="stylesheet" href="https://fonts.googleapis.com/css2?family=Cinzel:wght@500&family=Open+Sans:wght@400;600;700&display=swap">
<style>
  :root {
    --page-bg: #e9e6e1;
    --card-dark: #2a2a2b;
    --card-light: #ffffff;
    --brand-blue: #1f6fc2;
    --brand-blue-light: #4ea3ec;
    --brand-blue-deep: #0d5aa8;
    --mark-grey: #8d8f93;
    --ink: #1b1b1b;
    --white: #ffffff;
  }
  * { box-sizing: border-box; margin: 0; padding: 0; }
  html, body { width: 1200px; height: 901px; overflow: hidden; }
  body {
    background: var(--page-bg);
    font-family: "Open Sans", Arial, sans-serif;
    position: relative;
  }
  .card {
    position: absolute;
    left: 320px;
    width: 560px;
    height: 320px;
    border-radius: 4px;
    overflow: hidden;
    box-shadow: 0 6px 18px rgba(0,0,0,0.18);
  }
  .card--front { top: 110px; background: var(--card-dark); }
  .card--back { top: 470px; background: var(--card-light); }

  .brand {
    position: absolute;
    display: flex;
    flex-direction: column;
    align-items: center;
  }
  .brand__dot {
    width: 62px; height: 62px;
    border-radius: 50%;
    background: var(--mark-grey);
    margin-bottom: 12px;
  }
  .brand__name {
    font-family: "Cinzel", Georgia, serif;
    font-weight: 500;
    color: var(--brand-blue-light);
    text-align: center;
    letter-spacing: 1px;
    line-height: 1.15;
  }
  .card--front .brand { left: 0; right: 0; top: 96px; }
  .card--front .brand__name { font-size: 24px; }
  .card--back .brand { left: 318px; width: 220px; top: 90px; }
  .card--back .brand__name { font-size: 19px; color: var(--brand-blue); }

  .back-art { position: absolute; inset: 0; }

  .person {
    position: absolute;
    left: 22px; top: 48px;
    width: 245px;
    color: var(--white);
  }
  .person__name { font-size: 18px; font-weight: 700; line-height: 1.2; }
  .person__title { font-size: 12.5px; font-weight: 400; margin-top: 3px; line-height: 1.25; }

  .contact {
    position: absolute;
    left: 22px; top: 178px;
    list-style: none;
    color: var(--white);
    font-size: 10.5px;
    line-height: 1.25;
  }
  .contact__item { display: flex; align-items: center; gap: 7px; margin-bottom: 3px; white-space: nowrap; }
  .contact__icon { width: 11px; height: 11px; flex: none; }
</style>
</head>
<body>

  <section class="card card--front" aria-label="Card front">
    <div class="brand">
      <span class="brand__dot"></span>
      <span class="brand__name">KVRD Pinecrest Rehabilitation</span>
    </div>
  </section>

  <section class="card card--back" aria-label="Card back">
    <svg class="back-art" viewBox="0 0 560 320" width="560" height="320" aria-hidden="true">
      <defs>
        <radialGradient id="panelBlue" cx="35%" cy="45%" r="75%">
          <stop offset="0" stop-color="#4ea3ec"/>
          <stop offset="1" stop-color="#0d5aa8"/>
        </radialGradient>
      </defs>
      <path d="M0 0 H270 C330 40 250 120 270 190 C285 250 320 300 300 320 H0 Z" fill="url(#panelBlue)"/>
      <path d="M270 0 C330 40 250 120 270 190 C285 250 320 300 300 320" fill="none" stroke="#1b1b1b" stroke-width="4"/>
    </svg>

    <div class="person">
      <p class="person__name">Dorian K. Lumbard, Ph. D.</p>
      <p class="person__title">Vocational Rehabilitation Consultant</p>
    </div>

    <ul class="contact">
      <li class="contact__item">
        <svg class="contact__icon" viewBox="0 0 12 12"><path d="M6 1a3.5 3.5 0 0 0-3.5 3.5C2.5 7.5 6 11 6 11s3.5-3.5 3.5-6.5A3.5 3.5 0 0 0 6 1zm0 4.8a1.3 1.3 0 1 1 0-2.6 1.3 1.3 0 0 1 0 2.6z" fill="#fff"/></svg>
        <span>4173b GA Hwy 508 STE 612<br>Conyers, GA 30081</span>
      </li>
      <li class="contact__item">
        <svg class="contact__icon" viewBox="0 0 12 12"><path d="M3 1.5l1.6 2.2-.9 1a6 6 0 0 0 3.6 3.6l1-.9 2.2 1.6-.8 1.6C5.5 10.5 1.5 6.5 1.4 2.3z" fill="#fff"/></svg>
        <span>404-555-0142</span>
      </li>
      <li class="contact__item">
        <svg class="contact__icon" viewBox="0 0 12 12"><rect x="3" y="1" width="6" height="10" rx="1" fill="#fff"/></svg>
        <span>404-555-0187</span>
      </li>
      <li class="contact__item">
        <svg class="contact__icon" viewBox="0 0 12 12"><rect x="1.5" y="4" width="9" height="5" fill="#fff"/><rect x="3.5" y="1.5" width="5" height="3" fill="#fff"/></svg>
        <span>404-555-0163</span>
      </li>
      <li class="contact__item">
        <svg class="contact__icon" viewBox="0 0 12 12"><rect x="1" y="2.5" width="10" height="7" fill="#fff"/><path d="M1 2.5l5 4 5-4" fill="none" stroke="#1f6fc2" stroke-width="1"/></svg>
        <span>Dorian.Lumbard@kvrdpinecrestrehab.example</span>
      </li>
      <li class="contact__item">
        <svg class="contact__icon" viewBox="0 0 12 12"><circle cx="6" cy="6" r="5" fill="none" stroke="#fff" stroke-width="1.2"/><path d="M1 6h10M6 1c2 2.5 2 7.5 0 10M6 1c-2 2.5-2 7.5 0 10" fill="none" stroke="#fff" stroke-width="0.9"/></svg>
        <span>www.kvrdpinecrestrehab.example</span>
      </li>
    </ul>

    <div class="brand">
      <span class="brand__dot"></span>
      <span class="brand__name">KVRD Pinecrest Rehabilitation</span>
    </div>
  </section>

</body>
</html>
```